Letterhead design for ZENTORA company

I need an A4 letterhead design for my company "Zentora Electrical Products". I need the letterhead to match my current logo and business card designs. I would like it to be colourful and match the design of the business card in terms of the flowing line of colour where the information is.  

Target Market(s)

Adults aged 20 - 50 Upper middle class.

Industry/Entity Type

It Company

Requirements
Must have
• Must be A4 size and match my current logo and business card designs. Must be clean simple and eye catching.

• Must have the following information

• Zentora Electrical Products LTD
• 7 Ardley Close
• Chiswick
• London
• England
• W9 3QX
• Company No. 05316429
• VAT No. GB 627150384

• Telephone: 02081594360
• Mobile: 07815062247
• Email: info@zentora-goods.co.uk
Nice to have
• nice to have a wave of colour like the business card.
Should not have
• Should not be a different colour scheme to the business card and logo design.

```html
<!DOCTYPE html>
<html lang="en">
<head>
<meta charset="utf-8">
<title>Zentora Electrical Products – Letterhead</title>
<link rel="stylesheet" href="https://fonts.googleapis.com/css2?family=Didact+Gothic&family=Open+Sans:ital,wght@0,400;0,700;1,400&display=swap">
<style>
  :root {
    --teal-deep: #0a7fa3;
    --teal: #1596bd;
    --cyan: #34b3d8;
    --cyan-light: #7ed3ee;
    --paper: #ffffff;
    --ghost-grey: #e3e4e6;
    --ghost-grey-dark: #d6d8db;
    --ink-white: #ffffff;
    --label-white: #d8f2fb;
  }
  html, body {
    margin: 0;
    padding: 0;
    overflow: hidden;
    background: var(--paper);
  }
  .letterhead {
    position: relative;
    width: 854px;
    height: 1200px;
    overflow: hidden;
    background: var(--paper);
    font-family: "Open Sans", Arial, sans-serif;
  }
  .layer {
    position: absolute;
    left: 0;
    top: 0;
    width: 854px;
    height: 1200px;
  }
  .brand {
    position: absolute;
    left: 62px;
    top: 60px;
    color: var(--ink-white);
    font-family: "Didact Gothic", "Century Gothic", sans-serif;
  }
  .brand__name {
    display: block;
    font-size: 44px;
    line-height: 1;
    letter-spacing: 1px;
  }
  .brand__tagline {
    display: block;
    margin-top: 4px;
    font-size: 17px;
    letter-spacing: 0.5px;
  }
  .headline {
    position: absolute;
    right: 30px;
    top: 112px;
    margin: 0;
    text-align: right;
    font-family: "Didact Gothic", "Century Gothic", sans-serif;
    font-weight: 400;
    font-size: 64px;
    line-height: 0.85;
    letter-spacing: 10px;
    color: var(--ghost-grey);
  }
  .headline span { display: block; }
  .headline__first { margin-right: 26px; }
  .headline__second { margin-right: -10px; }
  .contact {
    position: absolute;
    left: 0;
    top: 0;
    width: 854px;
    height: 1200px;
    font-size: 10px;
    font-style: normal;
    line-height: 1;
    color: var(--ink-white);
  }
  .contact__line {
    position: absolute;
    margin: 0;
    white-space: nowrap;
    font-weight: 700;
    font-style: normal;
  }
  .contact__label {
    font-style: italic;
    font-weight: 400;
    color: var(--label-white);
  }
  .contact__value--large { font-size: 11px; }
</style>
</head>
<body>
<main class="letterhead">

  <svg class="layer ghost-name" viewBox="0 0 854 1200" aria-hidden="true">
    <defs>
      <linearGradient id="ghostFade" x1="0" y1="0" x2="0" y2="1">
        <stop offset="0" stop-color="var(--ghost-grey-dark)"/>
        <stop offset="1" stop-color="#f4f5f6"/>
      </linearGradient>
    </defs>
    <text x="91" y="1050" textLength="600" lengthAdjust="spacingAndGlyphs"
          font-family="Didact Gothic, Century Gothic, sans-serif"
          font-size="146" fill="url(#ghostFade)">ZENTORA</text>
  </svg>

  <svg class="layer wave" viewBox="0 0 854 1200" aria-hidden="true">
    <defs>
      <linearGradient id="topWave" x1="0" y1="0" x2="1" y2="1">
        <stop offset="0" stop-color="var(--teal-deep)"/>
        <stop offset="0.6" stop-color="var(--teal)"/>
        <stop offset="1" stop-color="var(--cyan)"/>
      </linearGradient>
      <linearGradient id="bottomWave" x1="0" y1="1" x2="1" y2="0">
        <stop offset="0" stop-color="var(--cyan)"/>
        <stop offset="0.5" stop-color="var(--teal)"/>
        <stop offset="1" stop-color="var(--teal-deep)"/>
      </linearGradient>
    </defs>

    <path d="M0,0 H612 C420,18 150,120 0,330 Z" fill="var(--cyan-light)"/>
    <path d="M0,0 H585 C400,22 140,122 0,318 Z" fill="var(--paper)"/>
    <path d="M0,0 H560 C380,26 130,126 0,306 Z" fill="var(--cyan)"/>
    <path d="M0,0 H520 C340,30 110,130 0,285 Z" fill="url(#topWave)"/>
    <path d="M0,285 C110,130 340,30 520,0 H470 C300,40 90,150 0,270 Z" fill="var(--teal-deep)" opacity="0.35"/>

    <path d="M250,1200 C520,1150 760,1050 854,900 V1200 Z" fill="var(--cyan-light)"/>
    <path d="M268,1200 C530,1158 770,1060 854,918 V1200 Z" fill="url(#bottomWave)"/>
  </svg>

  <div class="brand">
    <span class="brand__name">ZENTORA</span>
    <span class="brand__tagline">Electrical Products</span>
  </div>

  <h1 class="headline">
    <span class="headline__first">Electrical</span>
    <span class="headline__second">Products</span>
  </h1>

  <address class="contact">
    <p class="contact__line" style="right:31px; top:1058px;">Zentora Electrical Products LTD</p>
    <p class="contact__line" style="right:73px; top:1072px;">7 Ardley Close , Chiswick</p>
    <p class="contact__line" style="right:94px; top:1086px;">London , England , W9 3QX</p>
    <p class="contact__line contact__value--large" style="right:129px; top:1101px;"><span class="contact__label">Company No.</span>&nbsp; 05316429</p>
    <p class="contact__line contact__value--large" style="right:166px; top:1117px;"><span class="contact__label">VAT No.</span>&nbsp; GB 627150384</p>
    <p class="contact__line contact__value--large" style="right:209px; top:1133px;"><span class="contact__label">Phone:</span>&nbsp; 02081594360</p>
    <p class="contact__line contact__value--large" style="right:261px; top:1149px;"><span class="contact__label">Mobile:</span>&nbsp; 07815062247</p>
    <p class="contact__line" style="right:240px; top:1165px;"><span class="contact__label">Email:</span>&nbsp; info@zentora-goods.co.uk</p>
  </address>

</main>
</body>
</html>
```